Orthodox Christian Youth Conference Flyer/Agenda

We are seeking a designer to help us take our award winning conference to the next level with a pamphlet that will outline the agenda of the 3 day conference but will also include pictures, illustrations, and visuals so that we build some excitement and interest. We also need to be able to make adjustments and corrections to the pamphlet's text, leading up to the conference and would like it in a file that could permit us to edit it without having to bother you!

Target Market(s)

To be used to promote conference and agenda

Industry/Entity Type

Christian

Font styles to use
Serif
Sans Serif

Requirements
Must have
• include logo, photos and visuals

```html
<!DOCTYPE html>
<html lang="en">
<head>
<meta charset="utf-8">
<title>Youth and Family Conference 2015 Program</title>
<link href="https://fonts.googleapis.com/css2?family=Oswald:wght@500;700&family=Open+Sans:wght@400;600;700&family=Merriweather:wght@400;700&display=swap" rel="stylesheet">
<style>
:root{
  --lime:#8dc63f;
  --lime-dark:#6fa52a;
  --brown:#3b2518;
  --paper:#ffffff;
  --ink:#333333;
  --muted:#6b6b6b;
  --stage:#ece8e2;
}
*{margin:0;padding:0;box-sizing:border-box}
html,body{width:889px;height:1200px;overflow:hidden;background:var(--stage)}
body{position:relative;font-family:"Open Sans",Arial,sans-serif;color:var(--ink)}
.page{position:absolute;width:404px;height:552px;background:var(--paper);overflow:hidden;box-shadow:0 2px 8px rgba(0,0,0,.18)}
.page-1{left:30px;top:28px}
.page-2{left:455px;top:28px}
.page-3{left:30px;top:620px}
.page-4{left:455px;top:620px}
.abs{position:absolute}
.photo{position:absolute}
.heading{font-family:"Oswald",Arial,sans-serif;font-weight:700;text-transform:uppercase;letter-spacing:.5px;line-height:1}
.body-copy{font-size:6px;line-height:1.5;color:var(--ink)}
.body-copy p{margin-bottom:5px}
.body-copy b{color:var(--brown)}
.day-bar{background:var(--brown);color:#fff;font-family:"Oswald",Arial,sans-serif;font-size:6.5px;padding:3px 6px;margin:8px 0 4px}
.list{font-size:6px;line-height:1.75;list-style:none}
.list li::before{content:"• ";color:var(--lime-dark)}
.faq-q{font-weight:700;color:var(--lime-dark);font-size:6.5px;margin-top:7px}
.faq-a{font-size:6px;line-height:1.5}
.serif{font-family:"Merriweather",Georgia,serif}
</style>
</head>
<body>

<!-- Page 1: cover and agenda -->
<section class="page page-1">
  <div class="abs body-copy serif" style="left:14px;top:12px;width:200px">
    <div style="font-size:5.5px;color:var(--muted)">Cedar Hollow Fellowship Hall presents</div>
    <div style="font-size:9.5px;font-weight:700;color:var(--brown);line-height:1.25;margin-top:3px">THE 2015 ORTHODOX CHRISTIAN YOUTH AND FAMILY CONFERENCE</div>
    <div style="font-size:5.5px;margin-top:4px">Three days of worship, learning and fellowship for young people and families of every parish in our region.</div>
  </div>
  <div class="abs heading" style="left:262px;top:0;width:142px;height:60px;background:var(--lime);color:#fff;font-size:15px;padding:12px 10px;text-align:center">Description<br>of Event</div>
  <div class="photo" role="img" aria-label="Icon painting of saints" style="left:214px;top:60px;width:42px;height:56px;background:linear-gradient(#b8412e,#d9a441)"></div>
  <div class="abs body-copy" style="left:262px;top:66px;width:132px">
    <p>Our award winning gathering returns with services, talks, workshops and games for every age.</p>
    <p>Guests will share meals, sing together and meet friends from parishes near and far.</p>
  </div>

  <div class="abs" style="left:0;top:120px;width:250px;height:44px;background:var(--lime);color:#fff;padding:7px 14px">
    <div class="heading" style="font-size:17px">Program Agenda</div>
    <div style="font-size:6.5px;font-weight:600;margin-top:3px">for Youth and Family Conference 2015</div>
  </div>

  <div class="abs" style="left:14px;top:168px;width:236px">
    <div class="day-bar">Thursday, October 8th, 2015 · Arrival and Opening</div>
    <ul class="list">
      <li>4:00 PM Registration and welcome in the main hall</li>
      <li>5:00 PM Room check in and parish group photos</li>
      <li>6:00 PM Vespers followed by a shared family dinner</li>
      <li>8:00 PM Icebreaker games for youth and young adults</li>
    </ul>
    <div class="day-bar">Friday, October 9th, 2015 · Learning and Service</div>
    <ul class="list">
      <li>8:30 AM Morning prayers and breakfast together</li>
      <li>10:00 AM Keynote talk on faith in daily life</li>
      <li>1:00 PM Workshops by age group and parish service</li>
      <li>5:00 PM Choir rehearsal open to all singers</li>
      <li>7:00 PM Talent night and evening fellowship</li>
    </ul>
    <div class="day-bar">Saturday, October 10th, 2015 · Fellowship Day</div>
    <ul class="list">
      <li>9:00 AM Panel with clergy and open questions</li>
      <li>12:00 PM Picnic lunch and outdoor sports</li>
      <li>3:00 PM Service project in the local community</li>
      <li>6:00 PM Great Vespers and banquet dinner</li>
    </ul>
    <div class="day-bar">Sunday, October 11th, 2015 · Divine Liturgy</div>
    <ul class="list">
      <li>9:30 AM Divine Liturgy and closing blessing</li>
      <li>12:30 PM Farewell brunch and departures</li>
    </ul>
  </div>

  <div class="abs" style="left:262px;top:172px;width:142px;height:22px;background:var(--brown);color:#fff;font-size:6px;font-weight:700;padding:6px 8px">CEDAR HOLLOW FELLOWSHIP HALL</div>
  <div class="photo" role="img" aria-label="Photo of clergy leading a service" style="left:262px;top:200px;width:130px;height:110px;background:linear-gradient(#c9b48a,#6e5236)"></div>
  <div class="abs body-copy" style="left:262px;top:318px;width:130px">
    <p>All sessions take place in the fellowship hall unless noted on the schedule.</p>
    <p>Times may shift slightly; updates will be posted at the welcome desk each morning.</p>
  </div>
  <div class="photo" role="img" aria-label="Photo of conference participants" style="left:262px;top:440px;width:142px;height:112px;background:linear-gradient(#a7b98a,#4f5f3a)"></div>
</section>

<!-- Page 2: donations and program information -->
<section class="page page-2">
  <div class="photo" role="img" aria-label="Icon painting of a saint" style="left:14px;top:14px;width:70px;height:92px;background:linear-gradient(#c4472f,#e0b04f)"></div>
  <div class="abs" style="left:92px;top:14px;width:300px;height:100px;background:var(--brown);color:#fff;padding:8px 10px">
    <div style="font-size:9px;font-family:'Oswald',sans-serif">Opportunity to <span class="heading" style="font-size:14px;color:var(--lime)">Donate</span></div>
    <div style="font-size:5.6px;line-height:1.45;margin-top:5px;width:140px">Your gift keeps the conference affordable for every family. Donations cover meals, speakers, housing and scholarships for youth who could not attend otherwise.</div>
  </div>
  <div class="photo" role="img" aria-label="Photo of a lake and hills" style="left:250px;top:22px;width:134px;height:40px;background:linear-gradient(#9cc3d8,#55784a)"></div>
  <div class="photo" role="img" aria-label="Photo of the conference center" style="left:250px;top:66px;width:134px;height:42px;background:linear-gradient(#b3a18a,#5e4632)"></div>
  <div class="photo" role="img" aria-label="Photo of a church interior" style="left:14px;top:120px;width:120px;height:50px;background:linear-gradient(#d7b77a,#7a4e2e)"></div>
  <div class="photo" role="img" aria-label="Photo of a chapel sanctuary" style="left:140px;top:120px;width:120px;height:50px;background:linear-gradient(#c98f5a,#5a2f1d)"></div>

  <svg class="abs" style="left:0;top:176px" width="404" height="64" viewBox="0 0 404 64" aria-hidden="true">
    <rect x="0" y="0" width="404" height="52" fill="var(--brown)"/>
    <path d="M0 44 C120 62 280 30 404 48 L404 64 L0 64 Z" fill="var(--lime)"/>
  </svg>
  <div class="abs heading" style="left:24px;top:186px;color:#fff;font-size:15px;line-height:1.05">Program<br>Information</div>

  <div class="abs body-copy" style="left:14px;top:252px;width:180px">
    <p><b>Registration.</b> Register online or through your parish priest before September 20th to reserve rooms and meals for your family.</p>
    <p><b>Cost.</b> A modest fee covers lodging, all meals and materials. Group rates are offered for parishes sending ten or more people.</p>
    <p><b>What to bring.</b> Comfortable clothes, church attire for services, a water bottle and a prayer book.</p>
    <p><b>Housing.</b> Rooms are shared by age and family; chaperones stay on every floor.</p>
    <p><b>Check in.</b> Please arrive by 5:00 PM on Thursday so that every guest can settle in before Vespers.</p>
    <p><b>Safety.</b> All volunteers working with youth have completed parish safety training.</p>
  </div>
  <div class="abs body-copy" style="left:210px;top:252px;width:180px">
    <p><b>Speakers.</b> Clergy and lay teachers lead talks on prayer, friendship and service in the modern world.</p>
    <p><b>Youth tracks.</b> Separate sessions for children, teens and young adults run each day.</p>
    <p><b>Parking.</b> Free parking is available beside the hall and the chapel.</p>
    <p><b>Meals.</b> Fasting and dietary needs can be noted on the registration form.</p>
    <p><b>Bookstore.</b> Icons, books and gifts will be on sale in the lobby all weekend.</p>
    <p><b>Volunteers.</b> Helpers for meals, music and setup are always welcome; ask at the desk.</p>
  </div>
  <svg class="abs" style="left:0;top:492px" width="404" height="60" viewBox="0 0 404 60" aria-hidden="true">
    <path d="M0 24 C140 0 260 40 404 14 L404 60 L0 60 Z" fill="var(--lime)"/>
    <path d="M0 38 C140 18 260 54 404 30 L404 60 L0 60 Z" fill="var(--brown)"/>
  </svg>
</section>

<!-- Page 3: frequently asked questions -->
<section class="page page-3">
  <svg class="abs" style="left:0;top:0" width="404" height="90" viewBox="0 0 404 90" aria-hidden="true">
    <path d="M0 0 L230 0 C200 50 120 74 0 80 Z" fill="var(--lime)"/>
  </svg>
  <div class="abs heading" style="left:22px;top:14px;color:#fff;font-size:30px">FAQs</div>
  <div class="photo" role="img" aria-label="Photo of clergy processing in a church" style="left:232px;top:0;width:172px;height:122px;background:linear-gradient(#e6dccb,#8b6b4a)"></div>

  <div class="abs" style="left:14px;top:86px;width:210px">
    <div class="faq-q">Who can attend the conference?</div>
    <div class="faq-a">Everyone is welcome. Families, teens, young adults and friends from any parish are invited to join us.</div>
    <div class="faq-q">Is there an age limit for youth sessions?</div>
    <div class="faq-a">Youth tracks are grouped from ages six to twelve, thirteen to eighteen and young adults.</div>
  </div>
  <div class="abs" style="left:14px;top:150px;width:376px">
    <div class="faq-q">Do children need a chaperone?</div>
    <div class="faq-a">Yes, minors must attend with a parent or an approved parish chaperone for the whole weekend.</div>
    <div class="faq-q">Can I attend only one day?</div>
    <div class="faq-a">Day passes are available at the desk, though we encourage staying the whole weekend to share every service and meal.</div>
    <div class="faq-q">What if I have dietary needs?</div>
    <div class="faq-a">Please mark any fasting or allergy needs on your form and our kitchen team will prepare suitable meals.</div>
    <div class="faq-q">Are scholarships available?</div>
    <div class="faq-a">Yes. Thanks to generous donors, a number of scholarships help families cover the cost of attending.</div>
    <div class="faq-q">How do I get there?</div>
    <div class="faq-a">Directions and parking details are sent by email after registration, along with a packing list.</div>
    <div class="faq-q">Is there a dress code?</div>
    <div class="faq-a">Casual clothes are fine during the day; please bring modest church attire for services and the banquet.</div>
    <div class="faq-q">Can I bring a friend who is not Orthodox?</div>
    <div class="faq-a">Absolutely. Visitors are warmly welcomed to every talk, meal and service during the weekend.</div>
    <div class="faq-q">What happens if it rains?</div>
    <div class="faq-a">Outdoor games move into the gym and the picnic lunch is served in the fellowship hall.</div>
  </div>
  <div class="abs" style="left:14px;top:430px;width:258px">
    <div class="faq-q">Will there be confession during the weekend?</div>
    <div class="faq-a">Clergy will be available for confession on Saturday evening before Great Vespers.</div>
    <div class="faq-q">Can I cancel my registration?</div>
    <div class="faq-a">Fees are refunded in full for cancellations made before October 1st.</div>
    <div class="faq-q">Who do I contact with other questions?</div>
    <div class="faq-a">Reach the conference committee chair using the details on the back page.</div>
  </div>
  <div class="photo" role="img" aria-label="Photo of a priest blessing youth" style="left:282px;top:430px;width:122px;height:122px;background:linear-gradient(#c8b08c,#4f3a28)"></div>
</section>

<!-- Page 4: back cover and contact -->
<section class="page page-4">
  <div class="photo" role="img" aria-label="Group photo of conference families and clergy" style="left:0;top:0;width:404px;height:200px;background:linear-gradient(#b9a07e,#6b5440)"></div>
  <svg class="abs" style="left:0;top:170px" width="404" height="50" viewBox="0 0 404 50" aria-hidden="true">
    <path d="M0 20 C140 50 260 0 404 24 L404 50 L0 50 Z" fill="var(--lime)"/>
    <path d="M0 32 C140 58 260 12 404 36 L404 50 L0 50 Z" fill="var(--paper)"/>
  </svg>
  <div class="photo" role="img" aria-label="Photo of a brick church in winter" style="left:14px;top:226px;width:180px;height:230px;background:linear-gradient(#dfe6ec,#7a4a32)"></div>
  <div class="abs body-copy" style="left:206px;top:230px;width:184px">
    <p><b>Cedar Hollow Fellowship Hall</b><br>Hosting the Youth and Family Conference since 1998. Join us this autumn for three days of faith and friendship.</p>
  </div>
  <div class="photo" role="img" aria-label="Photo of the conference hall building" style="left:206px;top:300px;width:184px;height:150px;background:linear-gradient(#cfd9c0,#7d5a40)"></div>
  <div class="abs" style="left:14px;top:462px;width:180px;height:80px;background:var(--brown);color:#fff;font-size:5.8px;line-height:1.55;padding:8px">
    Cedar Hollow Orthodox Church<br>120 Chapel Road<br>Millbrook, PA 16000<br>youth@cedarhollowyouth.org
  </div>
  <div class="abs" style="left:206px;top:462px;width:198px;height:80px;background:var(--lime);color:#fff;font-size:7.5px;font-weight:700;line-height:1.35;padding:12px 10px">
    Contact Youth Conference Committee Chair, Daniel Marsh at youth@cedarhollowyouth.org or 555-014-2290 for further questions
  </div>
</section>

</body>
</html>
```